Fontenot Bayou Grillhouse (Owners Card)

Need a classy, but modern business card. I have included a promotional card for the steakhouse. I need one for myself (the owner) that is more professional.

Target Market(s)

General Public

Industry/Entity Type

Food service

Contact Information for Business Card

Name, business address, phone number, email, logo

Font styles to use
Serif
Sans Serif
Decorative
Script

Requirements
Must have
• My name (Darvel Pruitt), business address (327 Oakmere Street), phone number (510) 493-2615, email (Dpruittkr4@mailvane.example. On the back of the card: Psalms 27 1 The LORD is my light and my salvation— whom shall I fear? The LORD is the stronghold of my life— of whom shall I be afraid? 2 When the wicked advance against me to devour me, it is my enemies and my foes who will stumble and fall. 3 Though an army besiege me, my heart will not fear; though war break out against me, even then I will be confident.
Nice to have
• Something that’s bold, but modern and professional.

```html
<!DOCTYPE html>
<html lang="en">
<head>
<meta charset="utf-8">
<title>Fontenot Bayou Grillhouse – Owner Business Card</title>
<link rel="stylesheet" href="https://fonts.googleapis.com/css2?family=Montserrat:wght@400;500;600&display=swap">
<style>
  :root {
    --page: #ffffff;
    --card: #000000;
    --ink: #ffffff;
    --green-soft: #6db35a;
    --green: #6abf44;
    --lime: #b0d235;
    --amber: #f6a81c;
    --orange: #f15a29;
    --red: #ed1c24;
    --crimson: #d92030;
    --brand-name: #f6a81c;
    --brand-dot: #6abf44;
  }
  * { box-sizing: border-box; }
  html, body {
    margin: 0;
    width: 1200px;
    height: 875px;
    overflow: hidden;
    background: var(--page);
  }
  .canvas {
    position: relative;
    width: 1200px;
    height: 875px;
  }
  .card {
    position: absolute;
    left: 59px;
    top: 122px;
    width: 1077px;
    height: 623px;
    background: var(--card);
    overflow: hidden;
    font-family: "Montserrat", Arial, sans-serif;
  }
  .card-art {
    position: absolute;
    inset: 0;
    width: 1077px;
    height: 623px;
  }
  .brand {
    position: absolute;
    left: 60px;
    top: 150px;
    width: 480px;
    text-align: center;
  }
  .brand-dot {
    display: block;
    width: 110px;
    height: 110px;
    margin: 0 auto 26px;
    border-radius: 50%;
    background: var(--brand-dot);
  }
  .brand-name {
    margin: 0;
    font-weight: 500;
    font-size: 42px;
    line-height: 1.12;
    letter-spacing: 1px;
    color: var(--brand-name);
  }
  .contact {
    position: absolute;
    left: 590px;
    top: 165px;
    width: 470px;
    margin: 0;
    padding: 0;
    list-style: none;
    color: var(--ink);
    font-size: 25px;
    font-weight: 400;
    line-height: 36px;
    white-space: nowrap;
  }
  .contact-item {
    position: relative;
    padding-left: 42px;
    margin-bottom: 16px;
  }
  .contact-item.owner-name {
    font-size: 31px;
    font-weight: 600;
    line-height: 40px;
    margin-bottom: 20px;
  }
  .contact-icon {
    position: absolute;
    left: 0;
    top: 3px;
    width: 28px;
    height: 30px;
  }
</style>
</head>
<body>
<div class="canvas">
  <div class="card">
    <svg class="card-art" viewBox="0 0 1077 623" aria-hidden="true">
      <defs>
        <linearGradient id="spectrum" x1="0" y1="0" x2="1" y2="0">
          <stop offset="0" stop-color="var(--green-soft)"/>
          <stop offset="0.17" stop-color="var(--green)"/>
          <stop offset="0.4" stop-color="var(--lime)"/>
          <stop offset="0.58" stop-color="var(--amber)"/>
          <stop offset="0.75" stop-color="var(--orange)"/>
          <stop offset="0.9" stop-color="var(--red)"/>
          <stop offset="1" stop-color="var(--crimson)"/>
        </linearGradient>
        <linearGradient id="icon-grad" x1="0" y1="0" x2="1" y2="1">
          <stop offset="0" stop-color="var(--green)"/>
          <stop offset="0.55" stop-color="var(--amber)"/>
          <stop offset="1" stop-color="var(--red)"/>
        </linearGradient>
      </defs>
      <rect class="top-rule" x="0" y="41" width="1077" height="9" fill="url(#spectrum)"/>
      <path class="bottom-wave" fill="url(#spectrum)"
        d="M0 489 Q 380 600 770 538 C 795 533 805 520 830 536 C 850 550 872 548 893 540 C 925 527 965 556 1005 516 L 1077 489 L 1077 623 L 0 623 Z"/>
    </svg>

    <div class="brand">
      <span class="brand-dot"></span>
      <p class="brand-name">Fontenot Bayou<br>Grillhouse</p>
    </div>

    <ul class="contact">
      <li class="contact-item owner-name">Darvel Pruitt</li>
      <li class="contact-item">
        <svg class="contact-icon" viewBox="0 0 32 36" aria-hidden="true">
          <path d="M16 2 C8 2 3 8 3 14 C3 22 16 34 16 34 C16 34 29 22 29 14 C29 8 24 2 16 2 Z" fill="url(#icon-grad)"/>
          <circle cx="16" cy="14" r="5" fill="var(--card)"/>
        </svg>
        327 oakmere street<br>brookhaven, ca 94512
      </li>
      <li class="contact-item">
        <svg class="contact-icon" viewBox="0 0 32 36" aria-hidden="true">
          <g fill="none" stroke="url(#icon-grad)" stroke-width="2.6">
            <rect x="3" y="8" width="26" height="20" rx="2"/>
            <path d="M4 10 L16 20 L28 10"/>
          </g>
        </svg>
        Dpruittkr4@mailvane.example
      </li>
      <li class="contact-item">
        <svg class="contact-icon" viewBox="0 0 32 36" aria-hidden="true">
          <rect x="7" y="3" width="18" height="30" rx="3" fill="none" stroke="url(#icon-grad)" stroke-width="2.8"/>
          <line x1="13" y1="28" x2="19" y2="28" stroke="url(#icon-grad)" stroke-width="2.4"/>
        </svg>
        (510) 493-2615
      </li>
    </ul>
  </div>
</div>
</body>
</html>
```